Needing a business Card for new fire company.

Velm, sales fire equipment and parts. We also do tree clearing for the forest service. My logo will be attached to this. I am also looking for a design that when people see the card it stick with them and they will remember my sales team giving it to them.

```html
<!DOCTYPE html>
<html lang="en">
<head>
<meta charset="UTF-8">
<title>Velm Business Card</title>
<link rel="stylesheet" href="https://fonts.googleapis.com/css2?family=Open+Sans:wght@400;700;800&display=swap">
<style>
  :root {
    --bg: #2b2b2b;
    --white: #ffffff;
    --black: #0a0a0a;
    --red: #c0242e;
    --grey: #5a5a5a;
    --text-light: #f2f2f2;
  }
  * { box-sizing: border-box; margin: 0; padding: 0; }
  html, body {
    width: 1200px; height: 900px; overflow: hidden;
    background: var(--bg);
    font-family: "Open Sans", Arial, sans-serif;
  }
  .canvas { position: relative; width: 1200px; height: 900px; }
  .card {
    position: absolute; width: 700px; height: 400px; overflow: hidden;
    box-shadow: 0 14px 30px rgba(0,0,0,0.45);
  }
  .card-front { left: 110px; top: 40px; background: var(--white); }
  .card-back { left: 390px; top: 470px; background: var(--black); }
  .flame-area { position: absolute; inset: 0; width: 100%; height: 100%; }

  .brand-name {
    position: absolute; font-weight: 800; font-size: 110px;
    letter-spacing: 6px; line-height: 1; text-transform: uppercase;
  }
  .card-front .brand-name { left: 300px; top: 60px; color: var(--black); }
  .card-back .brand-name { left: 40px; top: 150px; color: var(--white); }

  .contact { position: absolute; color: var(--text-light); font-size: 17px; }
  .person { left: 40px; top: 36px; }
  .person .role { font-size: 17px; }
  .person .name { color: var(--red); font-weight: 700; font-size: 24px; letter-spacing: 1px; line-height: 1.1; }
  .line { display: flex; align-items: center; gap: 8px; line-height: 1.3; }
  .line svg { width: 16px; height: 16px; flex: none; fill: var(--red); }
  .address { left: 40px; top: 290px; }
  .online { left: 40px; top: 340px; }
</style>
</head>
<body>
<main class="canvas">

  <section class="card card-front" aria-label="Card front">
    <svg class="flame-area" viewBox="0 0 700 400" role="img" aria-label="Red flame illustration rising along the bottom">
      <path fill="var(--red)" d="M0 170 C60 150 80 230 140 200 C200 170 210 260 280 250 C350 240 380 290 460 280 C540 270 600 310 700 300 L700 400 L0 400 Z"/>
    </svg>
    <div class="brand-name">Velm</div>
  </section>

  <section class="card card-back" aria-label="Card back">
    <svg class="flame-area" viewBox="0 0 700 400" role="img" aria-label="Red flame illustration rising along the right side">
      <path fill="var(--red)" stroke="var(--grey)" stroke-width="4" d="M700 0 L540 0 C500 60 560 110 520 160 C480 210 430 190 420 240 C410 290 380 300 330 310 C280 320 300 370 260 400 L700 400 Z"/>
    </svg>

    <div class="contact person">
      <div class="role">Director</div>
      <div class="name">DARA QUILL</div>
      <div class="line">
        <svg viewBox="0 0 24 24" aria-hidden="true"><path d="M6.6 10.8a15 15 0 0 0 6.6 6.6l2.2-2.2a1 1 0 0 1 1-.25 11.4 11.4 0 0 0 3.6.57 1 1 0 0 1 1 1V20a1 1 0 0 1-1 1A17 17 0 0 1 3 4a1 1 0 0 1 1-1h3.5a1 1 0 0 1 1 1c0 1.25.2 2.45.57 3.57a1 1 0 0 1-.25 1z"/></svg>
        <span>(00) 0000 0000</span>
      </div>
    </div>

    <div class="brand-name">Velm</div>

    <div class="contact address">
      <div class="line">
        <svg viewBox="0 0 24 24" aria-hidden="true"><path d="M12 2a7 7 0 0 0-7 7c0 5.25 7 13 7 13s7-7.75 7-13a7 7 0 0 0-7-7zm0 9.5A2.5 2.5 0 1 1 12 6.5a2.5 2.5 0 0 1 0 5z"/></svg>
        <span>11 dummy city, dummy place<br>P.O Box 0000 Dummy Land</span>
      </div>
    </div>

    <div class="contact online">
      <div class="line">
        <svg viewBox="0 0 24 24" aria-hidden="true"><circle cx="12" cy="12" r="10"/></svg>
        <span>www.velm.com</span>
      </div>
      <div class="line">
        <svg viewBox="0 0 24 24" aria-hidden="true"><path d="M2 5h20v14H2z M2 5l10 8 10-8" stroke="var(--black)" stroke-width="1.5"/></svg>
        <span>dara@velm.com</span>
      </div>
    </div>
  </section>

</main>
</body>
</html>
```